Home page makeover

Take my existing home page, www.maplecrestharborline.com and redesign layout to look more current considering today's touch design prevalence.
Reuse existing elements or suggest improved ones if available.
I generally have average CSS and HTML skills using div containers, defining lists and using columns to create the code to support the layout.
Updates
Just wanted to send out a quick message to thank all of you for your submissions. Many of you offered nice designs, but unfortunately could only choose one.
Target Market(s)
Generally targeting individuals with some assets for retirement. Basically your average working professional or business owner.
Industry/Entity Type
It Support
Look and feel
Each slider illustrates characteristics of the customer's brand and the style your logo design should communicate.

```html
<!DOCTYPE html>
<html lang="en">
<head>
<meta charset="utf-8">
<title>Maplecrest Harborline – Home</title>
<link rel="stylesheet" href="https://fonts.googleapis.com/css2?family=Arimo:wght@400;700&family=Tinos:ital,wght@0,400;1,400;1,700&display=swap">
<style>
  :root {
    --ink: #222222;
    --ink-soft: #333333;
    --blue: #1a84e8;
    --green: #9ccc45;
    --green-dark: #1d4d14;
    --tab-grey: #e3e3e3;
    --rule: #cccccc;
    --frame: #e5e5e5;
    --panel-dark: #333333;
    --footer-link: #cfcfcf;
    --footer-text: #a9a9a9;
    --bubble: #efefef;
  }
  * { margin: 0; padding: 0; box-sizing: border-box; }
  html, body { width: 1108px; height: 1200px; overflow: hidden; background: #ffffff; }
  body { font-family: "Arimo", Arial, sans-serif; color: var(--ink); }
  .page {
    position: relative; width: 1200px; height: 1300px;
    transform: scale(0.92333); transform-origin: 0 0;
  }
  .abs { position: absolute; }

  /* Header */
  .brand { left: 110px; top: 62px; width: 350px; display: flex; align-items: center; gap: 12px; white-space: nowrap; }
  .brand-mark { width: 30px; height: 30px; background: var(--green); flex: none; }
  .brand-name { font-size: 28px; color: var(--green-dark); font-weight: 400; }
  .account { right: 87px; top: 18px; display: flex; align-items: center; font-size: 30px; color: var(--ink-soft); }
  .account a { color: inherit; text-decoration: none; }
  .account .divider { width: 2px; height: 54px; background: var(--ink-soft); margin: 0 10px 0 12px; }
  .main-nav { left: 479px; top: 89px; display: flex; gap: 6px; }
  .main-nav a {
    width: 208px; height: 64px; display: flex; align-items: center; justify-content: center;
    font-size: 28px; color: var(--ink-soft); background: var(--tab-grey); text-decoration: none;
  }
  .main-nav a.active { background: var(--green); color: #ffffff; }
  .header-bar { left: 84px; top: 153px; width: 1032px; height: 4px; background: var(--ink-soft); }

  /* Slider */
  .hero { left: 84px; top: 160px; width: 1032px; height: 330px; border: 3px solid var(--frame); background: #fff; }
  .hero-photo {
    position: absolute; left: 0; top: 0; width: 600px; height: 324px;
    background: linear-gradient(180deg, #9cc0e4 0%, #c8daea 45%, #d9d3c2 70%, #8d9a6e 100%);
    -webkit-mask-image: linear-gradient(90deg, #000 85%, transparent 100%);
            mask-image: linear-gradient(90deg, #000 85%, transparent 100%);
  }
  .hero-title { position: absolute; left: 628px; top: 30px; font-family: "Tinos", "Times New Roman", serif; font-style: italic; font-size: 104px; color: var(--blue); line-height: 1; }
  .cta {
    position: absolute; left: 692px; top: 152px; width: 284px; height: 70px;
    background: var(--green); border-radius: 10px; box-shadow: 2px 3px 0 var(--green-dark);
    display: flex; align-items: center; justify-content: center;
    font-size: 40px; color: var(--green-dark); text-decoration: none;
  }
  .pricing { position: absolute; left: 628px; top: 234px; list-style: none; font-family: "Tinos", "Times New Roman", serif; font-style: italic; font-size: 22px; color: var(--blue); line-height: 31px; }
  .pricing li::before { content: "•"; font-style: normal; margin-right: 6px; }
  .slider-arrows { position: absolute; left: 0; top: 0; }

  /* Welcome */
  .section-title { font-family: "Tinos", "Times New Roman", serif; font-size: 32px; color: var(--blue); font-weight: 400; }
  .welcome-title { left: 93px; top: 504px; }
  .rule { height: 1px; background: var(--rule); }
  .features { left: 90px; top: 555px; width: 1026px; list-style: none; font-size: 18px; line-height: 23px; color: var(--ink); white-space: nowrap; }
  .features li { position: relative; padding-left: 18px; }
  .features li::before { content: ""; position: absolute; left: 2px; top: 6px; width: 9px; height: 9px; border-radius: 50%; background: var(--ink-soft); }

  /* Testimonials */
  .testimonials-title { left: 92px; top: 862px; }
  .quote {
    left: 108px; top: 933px; width: 492px; height: 62px; background: var(--bubble); border-radius: 8px;
    padding: 6px 20px; font-size: 18px; line-height: 24px; color: #666;
  }
  .avatar { left: 99px; top: 1016px; width: 66px; height: 61px; background: var(--panel-dark); }
  .author { left: 174px; top: 1052px; font-size: 18px; color: var(--blue); }
  .video { left: 622px; top: 858px; width: 476px; height: 295px; background: var(--panel-dark); }

  /* Footer */
  .site-footer { left: 0; top: 1170px; width: 1200px; height: 130px; background: var(--panel-dark); }
  .footer-nav { position: absolute; left: 120px; top: 13px; display: flex; gap: 16px; font-size: 18px; }
  .footer-nav a { color: var(--footer-link); text-decoration: none; }
  .legal { position: absolute; left: 98px; top: 50px; width: 1000px; font-size: 13px; line-height: 16px; color: var(--footer-text); white-space: nowrap; }
</style>
</head>
<body>
<div class="page">

  <header>
    <div class="abs brand"><span class="brand-mark"></span><span class="brand-name">Maplecrest Harborline</span></div>
    <div class="abs account"><a href="#">Register</a><span class="divider"></span><a href="#">Log In</a></div>
    <nav class="abs main-nav">
      <a class="active" href="#">Home</a>
      <a href="#">About Us</a>
      <a href="#">Contact Us</a>
    </nav>
    <div class="abs header-bar"></div>
  </header>

  <section class="abs hero">
    <div class="hero-photo" role="img" aria-label="Photo of a rope hammock on a porch overlooking the beach"></div>
    <div class="hero-title">Retire</div>
    <a class="cta" href="#">Register Now</a>
    <ul class="pricing">
      <li>Only $19.99 For a One Year Membership</li>
      <li>Only $ 9.99 Per Year After That</li>
    </ul>
    <svg class="slider-arrows" width="1026" height="324" viewBox="0 0 1026 324">
      <circle cx="27" cy="111" r="19" fill="#e6e6e6" opacity="0.9"/>
      <path d="M31 102 L24 111 L31 120" fill="none" stroke="#ffffff" stroke-width="3"/>
      <circle cx="998" cy="110" r="19" fill="#e6e6e6"/>
      <path d="M994 101 L1001 110 L994 119" fill="none" stroke="#ffffff" stroke-width="3"/>
      <circle cx="980" cy="311" r="6" fill="#cccccc"/>
      <circle cx="996" cy="311" r="6" fill="#cccccc"/>
      <circle cx="1012" cy="311" r="6" fill="#1a84e8"/>
    </svg>
  </section>

  <h2 class="abs section-title welcome-title">Welcome to Maplecrest</h2>
  <div class="abs rule" style="left:84px;top:543px;width:1032px"></div>
  <ul class="abs features">
    <li>Identify and project your retirement needs and expectations including basic living expenses, housing costs,<br>recreation, big ticket non-recurring items, medical and nursing home care.</li>
    <li style="margin-top:27px">Identify and project all your sources of retirement income including retirement savings, other savings, pension plans,<br>Social Security, life insurance and working part-time during retirement for a period of time.</li>
    <li style="margin-top:22px">Strategize tapping into the equity of your real estate including swapping your primary residence for a different home<br>or retirement area, or selling and renting.</li>
    <li style="margin-top:14px">Produce easy to understand results featuring the Harbor Readiness Gauge™.</li>
    <li style="margin-top:11px">Save your work so you can return, revisit and edit your retirement plan at a later date.</li>
  </ul>

  <h2 class="abs section-title testimonials-title">Testimonials</h2>
  <svg class="abs" style="left:478px;top:868px" width="60" height="32" viewBox="0 0 60 32">
    <path d="M16 3 L6 16 L16 29" fill="none" stroke="#c8c8c8" stroke-width="5"/>
    <path d="M42 3 L52 16 L42 29" fill="none" stroke="#c8c8c8" stroke-width="5"/>
  </svg>
  <div class="abs rule" style="left:84px;top:904px;width:516px"></div>
  <blockquote class="abs quote">“ This site is a great place to get a handle on your retirement strategy. ”</blockquote>
  <svg class="abs" style="left:155px;top:994px" width="40" height="18" viewBox="0 0 40 18"><path d="M0 0 H36 L4 17 Z" fill="#efefef"/></svg>
  <div class="abs avatar" role="img" aria-label="Member profile picture placeholder"></div>
  <div class="abs author">Morgan, Vermont</div>

  <div class="abs video" role="img" aria-label="Introductory video">
    <svg width="476" height="295" viewBox="0 0 476 295"><path d="M196 102 L280 148 L196 195 Z" fill="#666666"/></svg>
  </div>

  <footer class="abs site-footer">
    <nav class="footer-nav"><a href="#">Home</a><a href="#">About Us</a><a href="#">Contact Us</a></nav>
    <p class="legal">We'd like to hear from you if you have any questions or comments regarding the content of this web-site. Just click on Contact above. Copyright 2013, Maplecrest<br>Harborline, Inc. All rights reserved. The "Harbor Readiness Gauge" is a Trademark of Maplecrest Harborline, Inc. All usage of this web-site is subject to the Terms and<br>Conditions of Use you agreed to upon when accessing your user account. It should be duly noted that you will have no claim of any kind against Maplecrest Harborline,<br>Inc. as a byproduct of using this web-site and gaining results from it, especially if you reside, are employed or have assets held outside of the United States.</p>
  </footer>

</div>
</body>
</html>
```